Meditation for IVF and infertility

I need a flyer inviting IVF patients to join my Meditation class, I would like to offer free meditation to ivf women and for couples this class is free every Thursday night at 5 pm
2465 west halloran blvd suite K Santa Barbara Ca 93274
larkvale-meditation.com for more details

```html
<!DOCTYPE html>
<html lang="en">
<head>
<meta charset="utf-8">
<title>Larkvale Meditation – Free Meditation Classes for IVF and Infertility</title>
<link rel="stylesheet" href="https://fonts.googleapis.com/css2?family=Questrial&family=Open+Sans:wght@400;600;700&display=swap">
<style>
  :root {
    --slate: #6b6b6e;
    --lilac: #cfb3cf;
    --lilac-deep: #b39bb0;
    --white: #ffffff;
    --ink-soft: #5a5a5c;
    --icon: #7a7a7c;
  }
  * { margin: 0; padding: 0; box-sizing: border-box; }
  html, body { width: 1011px; height: 1200px; overflow: hidden; background: var(--white); }
  .flyer { position: relative; width: 1011px; height: 1200px; overflow: hidden; font-family: "Open Sans", sans-serif; color: var(--white); }
  .flyer__shapes { position: absolute; inset: 0; width: 1011px; height: 1200px; }
  .brand {
    position: absolute; left: 673px; top: 444px; width: 240px; height: 240px;
    border: 3px solid var(--white); border-radius: 50%;
    display: flex; flex-direction: column; align-items: center; justify-content: center;
    font-family: "Questrial", sans-serif; color: var(--white); text-align: center;
  }
  .brand__name { font-size: 44px; line-height: 1; }
  .brand__tag { font-size: 18px; margin-top: 4px; margin-left: 70px; }
  .headline {
    position: absolute; left: 0; right: 0; top: 710px;
    font-family: "Questrial", sans-serif; font-weight: 400; font-size: 62px; line-height: 77px;
    text-align: center; letter-spacing: 0.5px;
  }
  .lede { position: absolute; left: 0; right: 0; top: 874px; text-align: center; font-size: 17px; font-weight: 600; }
  .schedule {
    position: absolute; left: 145px; top: 920px; width: 717px; height: 43px;
    background: var(--lilac-deep); border-radius: 22px;
    display: flex; align-items: center; justify-content: center;
    font-size: 24px; font-weight: 600; letter-spacing: 0.3px;
  }
  .venue { position: absolute; left: 0; right: 0; top: 993px; text-align: center; font-size: 21px; line-height: 28px; }
  .contacts { position: absolute; right: 32px; top: 1100px; list-style: none; color: var(--ink-soft); font-size: 19px; line-height: 29px; }
  .contacts__item { display: flex; align-items: center; justify-content: flex-end; gap: 8px; }
  .contacts__icon { width: 20px; height: 20px; }
</style>
</head>
<body>
<main class="flyer">
  <svg class="flyer__shapes" viewBox="0 0 612 790" preserveAspectRatio="none">
    <defs>
      <linearGradient id="photoTone" x1="0" y1="0" x2="0" y2="1">
        <stop offset="0" stop-color="#eef2f6"/>
        <stop offset="0.35" stop-color="#e2e6eb"/>
        <stop offset="0.6" stop-color="#d9d2da"/>
        <stop offset="0.8" stop-color="#c9cbd4"/>
        <stop offset="1" stop-color="#cfc8bb"/>
      </linearGradient>
      <linearGradient id="photoLight" x1="0" y1="0" x2="1" y2="0">
        <stop offset="0" stop-color="#ffffff" stop-opacity="0.35"/>
        <stop offset="0.5" stop-color="#ffffff" stop-opacity="0"/>
        <stop offset="1" stop-color="#ffffff" stop-opacity="0.3"/>
      </linearGradient>
      <linearGradient id="slateTone" x1="0" y1="0" x2="1" y2="1">
        <stop offset="0" stop-color="#707073"/>
        <stop offset="1" stop-color="#646467"/>
      </linearGradient>
    </defs>
    <g class="flyer__photo" role="img" aria-label="Photo of three women in pastel tops doing seated stretching and meditation on yoga mats in a bright studio">
      <rect x="0" y="0" width="612" height="450" fill="url(#photoTone)"/>
      <rect x="0" y="0" width="612" height="450" fill="url(#photoLight)"/>
    </g>
    <path class="flyer__wave-lilac" d="M0,358 C150,392 330,300 612,201 L612,231 C430,280 280,420 120,436 C70,440 30,432 0,418 Z" fill="var(--lilac)"/>
    <path class="flyer__panel" d="M0,418 C30,432 70,440 120,436 C280,420 430,280 612,231 L612,790 L0,790 Z" fill="url(#slateTone)"/>
    <path class="flyer__footer-edge" d="M270,790 C340,730 460,690 612,684 L612,790 Z" fill="var(--lilac-deep)"/>
    <path class="flyer__footer" d="M300,790 C365,738 470,698 612,692 L612,790 Z" fill="var(--white)"/>
  </svg>

  <div class="brand">
    <span class="brand__name">Larkvale</span>
    <span class="brand__tag">Meditation</span>
  </div>

  <h1 class="headline">Free Meditation Classes<br>for IVF and infertility</h1>
  <p class="lede">Free meditation to ivf women and for couples.</p>
  <p class="schedule">EVERY THURSDAY NIGHT AT 5 PM</p>
  <p class="venue">2465 west halloran blvd suite K Santa Barbara Ca 93274<br>larkvale-meditation.com for more details</p>

  <ul class="contacts">
    <li class="contacts__item">(555) 218-4470
      <svg class="contacts__icon" viewBox="0 0 20 20"><circle cx="10" cy="10" r="9" fill="var(--icon)"/><path d="M7 5.5 L8.6 5.5 L9.2 8 L8.2 8.8 C8.8 10.2 9.8 11.2 11.2 11.8 L12 10.8 L14.5 11.4 L14.5 13 C14.5 13.8 13.8 14.5 13 14.5 C9.4 14.3 5.7 10.6 5.5 7 C5.5 6.2 6.2 5.5 7 5.5 Z" fill="#fff"/></svg>
    </li>
    <li class="contacts__item">larkvalemeditation@mail.com
      <svg class="contacts__icon" viewBox="0 0 20 20"><circle cx="10" cy="10" r="9" fill="var(--icon)"/><rect x="5" y="6.5" width="10" height="7" rx="1" fill="#fff"/><path d="M5.5 7 L10 10.5 L14.5 7" fill="none" stroke="#7a7a7c" stroke-width="1"/></svg>
    </li>
    <li class="contacts__item">www.larkvale-meditation.com
      <svg class="contacts__icon" viewBox="0 0 20 20"><circle cx="10" cy="10" r="9" fill="var(--icon)"/><g fill="none" stroke="#fff" stroke-width="1"><circle cx="10" cy="10" r="5.5"/><ellipse cx="10" cy="10" rx="2.4" ry="5.5"/><path d="M4.5 10 H15.5 M5.3 7.3 H14.7 M5.3 12.7 H14.7"/></g></svg>
    </li>
  </ul>
</main>
</body>
</html>
```